GUARANTEED! Simple website for independent event planner and consultant...

I need a website that is no more than 5 or 6 pages to illustrate who I am and what I can offer to groups who book hotels for meetings and conferences. I have 20 years of experience planning meetings within hotels and I am now ready to go out on my own and help clients choose venues, negotiate contracts and plan effective meetings. I will focus on clients planning meetings in the mountains of Colorado but I am willing to travel as well. I want to work with a person who is collaborative and can direct me on what they need to move the project along quickly. I already have my logo, a hosting site and work e-mail address. Also, I recently hired a photographer to do head shots. Lastly, it important for me to be able to talk on the phone or skype with this person, as needed and I must be able to make changes to my site down the road when necessary...

Target Market(s)

Corporate Groups

Industry/Entity Type

Event Planning

Coding

Coded - Design and coding required

Number of Pages Required

5+ page

Font styles to use
Sans Serif

Requirements
Must have
• About me page, event planning services offered page, task force and consulting work page, testimonials page, page for blogs, page to contact me/request a proposal. May need advice on what else I need...
Nice to have
• I want it to look sharp and professional. I want people to look at my site and know immediately that they can trust me and the work I can do.
• I don't want it to look like it is over the top as I am not a HUGE company but I do want it to be professional and easy to view and navigate.
Should not have
• Bright colors
• My logo is bright orange and black. I have also used dark grey and orange. See below:
• Orange:
• C = 0
• M = 64
• Y = 100
• K = 0
• Gray:
• C = 67
• M = 60
• Y = 59
• K = 45
• Font: Gotham Book and Gotham Bold

```html
<!DOCTYPE html>
<html lang="en">
<head>
<meta charset="utf-8">
<title>Alder Events Management</title>
<link href="https://fonts.googleapis.com/css2?family=Montserrat:wght@300;400;500;600;700;800&display=swap" rel="stylesheet">
<style>
:root{
  --orange:#f47b20;
  --orange-dark:#d9650f;
  --ink:#2b2b2d;
  --charcoal:#3a3a3c;
  --night:#1e1e20;
  --grey:#7a7a7c;
  --light:#f2f2f2;
  --white:#ffffff;
}
*{box-sizing:border-box;margin:0;padding:0}
html,body{width:1200px;height:3836px;overflow:hidden}
body{font-family:'Montserrat',sans-serif;color:var(--ink);background:var(--white);position:relative}
.photo{display:block}
.btn{display:inline-block;font-size:11px;font-weight:600;text-transform:uppercase;padding:11px 26px;border-radius:2px}
.btn-orange{background:var(--orange);color:var(--white)}
.btn-outline{border:1px solid currentColor}
.section-title{font-size:34px;font-weight:700;text-transform:uppercase;text-align:center;letter-spacing:1px}
.rule{width:70px;height:3px;background:var(--orange);margin:10px auto 0}

/* top bar + nav */
.topbar{position:absolute;top:0;left:0;width:1200px;height:28px;background:var(--night);color:#ccc;font-size:10px;display:flex;justify-content:flex-end;align-items:center;gap:26px;padding-right:150px}
.topbar b{color:var(--orange);font-weight:600}
.nav{position:absolute;top:28px;left:0;width:1200px;height:68px;background:var(--white);display:flex;align-items:center;justify-content:space-between;padding:0 150px;box-shadow:0 2px 6px rgba(0,0,0,.12);z-index:3}
.brand{display:flex;align-items:center;gap:10px}
.brand-mark{width:14px;height:14px;background:var(--orange)}
.brand-name{font-size:18px;font-weight:700;text-transform:uppercase;color:var(--ink)}
.menu{display:flex;gap:22px;font-size:11px;font-weight:500;color:var(--charcoal)}
.menu .active{color:var(--orange)}

/* hero */
.hero{position:absolute;top:96px;left:0;width:1200px;height:384px}
.hero-copy{position:absolute;top:140px;left:0;width:1200px;text-align:center;color:var(--white)}
.hero-copy h1{font-size:44px;font-weight:700;text-transform:uppercase;letter-spacing:2px;line-height:1.05}
.hero-copy h1 span{font-weight:300;display:block}
.hero-copy p{font-size:12px;width:560px;margin:14px auto 22px;line-height:1.5;color:#eee}
.hero-copy .btn{margin:0 8px}

/* about */
.about{position:absolute;top:480px;left:0;width:1200px;height:410px}
.about-text{position:absolute;left:270px;top:60px;width:400px}
.about-text h2{font-size:28px;font-weight:700;color:var(--orange);text-transform:uppercase}
.about-text .lead{font-size:14px;font-weight:600;margin:12px 0;line-height:1.4}
.about-text p{font-size:11px;line-height:1.65;color:var(--grey);margin-bottom:10px}
.about-text .btns{margin-top:16px;display:flex;gap:14px}
.about-text .btn-outline{color:var(--orange)}
.about-frame{position:absolute;left:690px;top:50px;width:260px;height:320px;border:5px solid var(--orange)}

/* events */
.events{position:absolute;top:890px;left:0;width:1200px;height:600px;background:radial-gradient(ellipse at 50% 45%,#8a4a1c 0%,#3a2418 45%,#151414 85%)}
.events .section-title{color:var(--white);padding-top:48px}
.event-cards{position:absolute;top:150px;left:90px;display:flex;gap:10px}
.event-card{width:196px;height:230px;position:relative}
.event-card .date{position:absolute;bottom:14px;left:12px;color:var(--white);font-size:21px;font-weight:700}
.event-meta{position:absolute;top:388px;left:90px;display:flex;gap:10px}
.event-meta div{width:196px;display:flex;align-items:center;gap:8px;font-size:10px;color:#ccc}
.dot{width:14px;height:14px;border-radius:50%;background:var(--orange)}
.events .arrow{position:absolute;top:448px;width:24px;height:24px}
.events .btn{position:absolute;top:440px;left:540px}

/* services */
.services{position:absolute;top:1490px;left:0;width:1200px;height:470px;background:linear-gradient(#f6f6f6,#e9e9e9)}
.services .section-title{color:var(--orange);padding-top:50px}
.service-list{position:absolute;top:150px;left:260px;display:flex;gap:80px}
.service{width:170px;text-align:center}
.service .photo{margin:0 auto;border:4px solid var(--white);border-radius:50%;box-shadow:0 2px 6px rgba(0,0,0,.2)}
.service h3{font-size:16px;font-weight:500;margin-top:16px}
.service h3 span{display:block;color:var(--orange);font-weight:700;text-transform:uppercase}
.service small{display:block;font-size:9px;font-weight:700;margin-top:8px;text-transform:uppercase}
.chev{position:absolute;top:220px;width:28px;height:28px;border:1px solid #bbb;border-radius:50%}

/* consulting */
.consulting{position:absolute;top:1960px;left:0;width:1200px;height:460px}
.consulting .section-title{color:var(--orange);padding-top:30px}
.grid{position:absolute;left:90px;top:100px;width:560px;height:340px}
.grid .photo{position:absolute}
.consult-copy{position:absolute;left:790px;top:180px;width:260px;text-align:center}
.consult-copy h3{font-size:19px;font-weight:700;text-transform:uppercase;color:var(--orange);line-height:1.2}
.consult-copy h3 span{color:var(--ink);display:block}
.consult-copy small{display:block;font-size:9px;margin:8px 0 14px;color:var(--grey);text-transform:uppercase}

/* testimonials */
.testimonials{position:absolute;top:2420px;left:0;width:1200px;height:340px;background:linear-gradient(#e4e4e4,#f3f3f3)}
.testimonials .section-title{padding-top:40px}
.avatars{position:absolute;left:280px;top:120px;display:flex;flex-direction:column;gap:14px}
.avatar{display:block;width:44px;height:44px;border-radius:50%;border:3px solid var(--white)}
.avatar.on{border-color:var(--orange)}
.quote{position:absolute;left:350px;top:120px;width:440px;background:var(--charcoal);color:#ddd;padding:22px 26px;font-size:11px;line-height:1.65}
.quote p+p{margin-top:10px}
.quote::before{content:"";position:absolute;left:-14px;top:76px;border:14px solid transparent;border-left:0;border-right-color:var(--charcoal)}
.names{position:absolute;left:820px;top:140px;font-size:11px;color:var(--grey);line-height:2.1}
.names .on{color:var(--orange);font-weight:600}

/* blog */
.blog{position:absolute;top:2760px;left:0;width:1200px;height:600px;background:var(--orange)}
.blog .section-title{color:var(--white);padding-top:44px}
.post{position:absolute;width:215px;height:220px;background:var(--white);display:flex;flex-direction:column}
.post .body{padding:12px 12px;font-size:9px;color:var(--grey);line-height:1.5}
.post h4{font-size:12px;font-weight:700;color:var(--ink);text-transform:uppercase;line-height:1.25;margin-bottom:4px}
.post .more{color:var(--orange);font-weight:600;margin-top:4px;display:block}

/* footer */
.footer{position:absolute;top:3360px;left:0;width:1200px;height:440px;background:radial-gradient(ellipse at 30% 40%,#3a3a3a,#1a1a1a 80%);color:#ddd}
.footer h2{position:absolute;left:130px;top:70px;font-size:40px;font-weight:700;color:var(--white);line-height:1}
.footer h2 span{display:block;font-weight:300;font-size:30px;margin-top:4px}
.form{position:absolute;left:130px;top:170px;width:500px}
.field{border-bottom:1px solid #666;height:34px;font-size:10px;color:#999;padding-top:14px}
.field.msg{height:76px}
.form .btn{margin-top:18px}
.foot-brand{position:absolute;left:790px;top:70px}
.foot-brand p{font-size:10px;line-height:1.6;color:#aaa;margin-top:12px;width:280px}
.contact{position:absolute;left:790px;top:220px;font-size:11px;line-height:2.1;display:flex;flex-direction:column}
.contact span{display:flex;align-items:center;gap:10px}
.join{position:absolute;left:790px;top:300px}
.join h3{font-size:18px;font-weight:700;color:var(--white)}
.socials{display:flex;gap:10px;margin-top:12px}
.socials i{width:32px;height:32px;border-radius:50%;background:var(--white);display:block}
.bottombar{position:absolute;top:3800px;left:0;width:1200px;height:36px;background:var(--orange);color:var(--white);font-size:10px;display:flex;justify-content:space-between;align-items:center;padding:0 130px}
</style>
</head>
<body>

<div class="topbar"><span>Phone Number: <b>(303) 555-0148</b></span><span>Email: <b>hello@alderevents.com</b></span></div>
<header class="nav">
  <div class="brand"><span class="brand-mark"></span><span class="brand-name">Alder</span></div>
  <nav class="menu"><span class="active">Home</span><span>About Us</span><span>Event Planning Services</span><span>Testimonials</span><span>Blogs</span><span>Contact Us</span></nav>
</header>

<section class="hero">
  <svg class="photo" width="1200" height="384" role="img" aria-label="Audience seated in a conference hall listening to a speaker"><defs><linearGradient id="hg" x1="0" y1="0" x2="1" y2="1"><stop offset="0" stop-color="#9a9a9c"/><stop offset=".5" stop-color="#6b6360"/><stop offset="1" stop-color="#4a4240"/></linearGradient></defs><rect width="1200" height="384" fill="url(#hg)"/><rect width="1200" height="384" fill="#000" opacity=".25"/></svg>
  <div class="hero-copy">
    <h1>Hotels for Meetings <span>and Conferences</span></h1>
    <p>Lorem ipsum is simply dummy text of the printing and typesetting industry, used by planners since the early days of print and layout.</p>
    <span class="btn btn-orange">Read More</span><span class="btn btn-orange">Explore Now</span>
  </div>
</section>

<section class="about">
  <div class="about-text">
    <h2>About the Conference</h2>
    <p class="lead">Lorem Ipsum is simply dummy text of the printing and typesetting industry.</p>
    <p>Lorem Ipsum is simply dummy text of the printing and typesetting industry. Lorem Ipsum has been the industry's standard dummy text ever since the 1500s, when an unknown printer took a galley of type and scrambled it to make a type specimen book.</p>
    <p>Lorem Ipsum is simply dummy text of the printing and typesetting industry. It has survived not only five centuries, but also the leap into electronic typesetting, remaining essentially unchanged.</p>
    <div class="btns"><span class="btn btn-outline">Read More</span><span class="btn btn-orange">Say Hello</span></div>
  </div>
  <svg class="about-frame photo" width="260" height="320" role="img" aria-label="Portrait of the event planner in business attire"><rect width="260" height="320" fill="#d6d2cf"/><rect y="140" width="260" height="180" fill="#3c3a3a" opacity=".55"/></svg>
</section>

<section class="events">
  <h2 class="section-title">Events Planning</h2><div class="rule"></div>
  <div class="event-cards">
    <div class="event-card"><svg class="photo" width="196" height="230" role="img" aria-label="Event photo: speaker portrait"><rect width="196" height="230" fill="#7c7472"/></svg><span class="date">Oct.20.2017</span></div>
    <div class="event-card"><svg class="photo" width="196" height="230" role="img" aria-label="Event photo: delegates at a meeting"><rect width="196" height="230" fill="#6a6c70"/></svg><span class="date">Sep.21.2017</span></div>
    <div class="event-card"><svg class="photo" width="196" height="230" role="img" aria-label="Event photo: conference audience"><rect width="196" height="230" fill="#5f5c5e"/></svg><span class="date">Aug.15.2017</span></div>
    <div class="event-card"><svg class="photo" width="196" height="230" role="img" aria-label="Event photo: presenter on stage"><rect width="196" height="230" fill="#736862"/></svg><span class="date">July.10.2017</span></div>
    <div class="event-card"><svg class="photo" width="196" height="230" role="img" aria-label="Event photo: evening reception with stage lights"><rect width="196" height="230" fill="#4f4460"/></svg><span class="date">June.30.2017</span></div>
  </div>
  <div class="event-meta"><div><i class="dot"></i>Read More</div><div><i class="dot"></i>Read More</div><div><i class="dot"></i>Read More</div><div><i class="dot"></i>Read More</div><div><i class="dot"></i>Read More</div></div>
  <svg class="arrow" style="left:90px" viewBox="0 0 24 24"><rect width="24" height="24" fill="#f47b20"/><path d="M14 7l-5 5 5 5" stroke="#fff" stroke-width="2" fill="none"/></svg>
  <span class="btn btn-orange">See All Events</span>
  <svg class="arrow" style="left:1086px" viewBox="0 0 24 24"><rect width="24" height="24" fill="#f47b20"/><path d="M10 7l5 5-5 5" stroke="#fff" stroke-width="2" fill="none"/></svg>
</section>

<section class="services">
  <h2 class="section-title">Our Services</h2><div class="rule"></div>
  <svg class="chev" style="left:180px" viewBox="0 0 28 28"><path d="M16 9l-5 5 5 5" stroke="#999" stroke-width="2" fill="none"/></svg>
  <div class="service-list">
    <div class="service"><svg class="photo" width="170" height="170" role="img" aria-label="Group seated around a meeting table"><circle cx="85" cy="85" r="85" fill="#9a8f86"/></svg><h3>Meetings and <span>Conferences</span></h3><small>Read More</small></div>
    <div class="service"><svg class="photo" width="170" height="170" role="img" aria-label="Planning meeting with a presenter"><circle cx="85" cy="85" r="85" fill="#8c9098"/></svg><h3>Planning <span>Meetings</span></h3><small>Read More</small></div>
    <div class="service"><svg class="photo" width="170" height="170" role="img" aria-label="Microphone on stage at an event"><circle cx="85" cy="85" r="85" fill="#5e5a58"/></svg><h3>EventPlanning <span>Services</span></h3><small>Read More</small></div>
  </div>
  <svg class="chev" style="left:992px" viewBox="0 0 28 28"><path d="M12 9l5 5-5 5" stroke="#999" stroke-width="2" fill="none"/></svg>
</section>

<section class="consulting">
  <h2 class="section-title">Consulting Work</h2>
  <div class="grid">
    <svg class="photo" style="left:0;top:0" width="180" height="150" role="img" aria-label="Consulting team discussion"><rect width="180" height="150" fill="#a89a8c"/></svg>
    <svg class="photo" style="left:190px;top:0" width="180" height="150" role="img" aria-label="Consultant presenting to clients"><rect width="180" height="150" fill="#8c95a0"/></svg>
    <svg class="photo" style="left:0;top:160px" width="180" height="170" role="img" aria-label="Business group at a workshop"><rect width="180" height="170" fill="#9aa2a8"/></svg>
    <svg class="photo" style="left:190px;top:160px" width="180" height="170" role="img" aria-label="Seated conference audience"><rect width="180" height="170" fill="#7f7872"/></svg>
    <svg class="photo" style="left:380px;top:90px" width="180" height="240" role="img" aria-label="Speaker addressing a meeting room"><rect width="180" height="240" fill="#a6978a"/></svg>
  </div>
  <div class="consult-copy">
    <h3>Hotels for Meetings <span>and Conferences</span></h3>
    <small>Watch Video</small>
    <svg width="46" height="46" viewBox="0 0 46 46"><circle cx="23" cy="23" r="21" fill="none" stroke="#f47b20" stroke-width="2"/><path d="M18 14l13 9-13 9z" fill="#f47b20"/></svg>
  </div>
</section>

<section class="testimonials">
  <h2 class="section-title">Testimonials</h2>
  <div class="avatars">
    <svg class="avatar" viewBox="0 0 44 44" role="img" aria-label="Client portrait"><circle cx="22" cy="22" r="22" fill="#b7a08e"/></svg>
    <svg class="avatar on" viewBox="0 0 44 44" role="img" aria-label="Client portrait"><circle cx="22" cy="22" r="22" fill="#7a5c4e"/></svg>
    <svg class="avatar" viewBox="0 0 44 44" role="img" aria-label="Client portrait"><circle cx="22" cy="22" r="22" fill="#c9b29a"/></svg>
  </div>
  <div class="quote">
    <p>Lorem Ipsum is simply dummy text of the printing and typesetting industry. Lorem Ipsum has been the industry's standard dummy text ever since the 1500s, when an unknown printer took a galley of type and scrambled it.</p>
    <p>Lorem Ipsum is simply dummy text of the printing and typesetting industry. Lorem Ipsum has been the industry's standard dummy text ever since the 1500s.</p>
  </div>
  <div class="names"><div>Sarah Lind</div><div class="on">Mark Olsen</div><div>Dana Pierce</div><div>Owen Breck</div></div>
</section>

<section class="blog">
  <h2 class="section-title">Latest Blog</h2><div class="rule" style="background:#fff"></div>
  <svg class="photo" style="position:absolute;left:175px;top:140px" width="205" height="150" role="img" aria-label="Colleagues reviewing documents"><rect width="205" height="150" fill="#b3a99e"/></svg>
  <div class="post" style="left:385px;top:140px"><div class="body"><h4>Engineering, Energy &amp; Operation Optimization</h4>June 21,2017<br>Lorem ipsum dolor sit amet, consectetur adipiscing elit, sed do eiusmod tempor incididunt ut labore et dolore magna aliqua.<span class="more">Read More</span></div></div>
  <svg class="photo" style="position:absolute;left:615px;top:140px" width="205" height="150" role="img" aria-label="Team meeting at a table"><rect width="205" height="150" fill="#8f8a86"/></svg>
  <div class="post" style="left:825px;top:140px"><div class="body"><h4>Engineering, Energy &amp; Operation Optimization</h4>June 21,2017<br>Lorem ipsum dolor sit amet, consectetur adipiscing elit, sed do eiusmod tempor incididunt ut labore et dolore magna aliqua.<span class="more">Read More</span></div></div>
  <div class="post" style="left:175px;top:365px"><div class="body"><h4>Engineering, Energy &amp; Operation Optimization</h4>June 21,2017<br>Lorem ipsum dolor sit amet, consectetur adipiscing elit, sed do eiusmod tempor incididunt ut labore et dolore magna aliqua.<span class="more">Read More</span></div></div>
  <svg class="photo" style="position:absolute;left:395px;top:365px" width="205" height="150" role="img" aria-label="Office team at work"><rect width="205" height="150" fill="#a0a4a6"/></svg>
  <div class="post" style="left:615px;top:365px"><div class="body"><h4>Engineering, Energy &amp; Operation Optimization</h4>June 21,2017<br>Lorem ipsum dolor sit amet, consectetur adipiscing elit, sed do eiusmod tempor incididunt ut labore et dolore magna aliqua.<span class="more">Read More</span></div></div>
  <svg class="photo" style="position:absolute;left:835px;top:365px" width="205" height="150" role="img" aria-label="Presenter at a whiteboard"><rect width="205" height="150" fill="#9c8c80"/></svg>
</section>

<footer class="footer">
  <h2>ALDER <span>EVENTS MANAGEMENT</span></h2>
  <div class="form">
    <div class="field">Name</div><div class="field">Email</div><div class="field">Phone</div><div class="field msg">Message</div>
    <span class="btn btn-orange">Submit</span>
  </div>
  <div class="foot-brand">
    <div class="brand"><span class="brand-mark"></span><span class="brand-name" style="color:#fff">Alder</span></div>
    <p>Helping groups choose venues, negotiate hotel contracts and plan effective meetings in the Colorado mountains and beyond.</p>
  </div>
  <div class="contact">
    <span><svg width="14" height="14" viewBox="0 0 14 14"><rect x="1" y="3" width="12" height="8" fill="none" stroke="#f47b20"/><path d="M1 3l6 5 6-5" stroke="#f47b20" fill="none"/></svg>hello@alderevents.com</span>
    <span><svg width="14" height="14" viewBox="0 0 14 14"><path d="M3 1h3l1 3-2 1a7 7 0 004 4l1-2 3 1v3c-6 1-11-4-10-10z" fill="#f47b20"/></svg>+1 (303) 555-0148</span>
  </div>
  <div class="join"><h3>JOIN US ON</h3><div class="socials"><i></i><i></i><i></i><i></i><i></i><i></i></div></div>
</footer>
<div class="bottombar"><span>Copyright © 2017 Alder Events Management. All Rights Reserved.</span><span>Website &amp; Hosting by Alder Web Studio</span></div>

</body>
</html>
```